Revamp of existing namecard

Existingly, i've got a namecard that i would like to retain the main design. but there are some changes in my company and i would need to do some amendments to it.

We are a money transfer and money exchange company.
I need 2 different types of name card.
1. For individual name cards
the front to put the following:
Company name and logo
English Name, Chinese Name appointment
Mobile Number, Email and Website.
2 License number under the logo and name

the back of the name card to put
8 address: 7 Singapore and 1 Hong Kong branch addresses
8 Mobile Number of the corresponding addresses.

We would like to retain the name card front design
the name card back design can change but color to retain.

2nd name card is generic name card
Front:
Company name and logo
Branch Mobile Number, Branch Address, Email and Website.

Industry/Entity Type

remittance and money exchange

Contact Information for Business Card

I need 2 different types of name card. 1. For individual name cards the front to put the following: Company name and logo English Name, Chinese Name appointment Mobile Number, Email and Website. 2 License number under the logo and name the back of the name card to put 8 address: 7 Singapore and 1 Hong Kong branch addresses 8 Mobile Number of the corresponding addresses. We would like to retain the name card front design the name card back design can change but color to retain. 2nd name card is generic name card Front: the front to put the following: Company name and logo Branch Mobile Number, Branch Address, Email and Website. 2 License number under the logo and name

Requirements
Must have
• I need 2 different types of name card. 1. For individual name cards the front to put the following: Company name and logo English Name, Chinese Name appointment Mobile Number, Email and Website. 2 License number under the logo and name the back of the name card to put 8 address: 7 Singapore and 1 Hong Kong branch addresses 8 Mobile Number of the corresponding addresses. We would like to retain the name card front design the name card back design can change but color to retain. 2nd name card is generic name card Front: the front to put the following: Company name and logo Branch Mobile Number, Branch Address, Email and Website. 2 License number under the logo and name
Nice to have
• use back color code

```html
<!DOCTYPE html>
<html lang="en">
<head>
<meta charset="utf-8">
<title>Meridan Name Cards</title>
<link href="https://fonts.googleapis.com/css2?family=Montserrat:wght@400;500;600&family=Noto+Sans+TC:wght@700&display=swap" rel="stylesheet">
<style>
  :root {
    --stage: #939393;
    --paper: #ffffff;
    --navy: #263340;
    --ink: #2a3440;
    --teal: #6cc5d6;
    --map: #e4e4e4;
    --rule: #5d6b78;
  }
  * { margin: 0; padding: 0; box-sizing: border-box; }
  html, body { width: 1200px; height: 1000px; overflow: hidden; }
  body {
    background: var(--stage);
    font-family: "Montserrat", Arial, sans-serif;
    position: relative;
  }
  .card {
    position: absolute;
    width: 537px;
    height: 309px;
    box-shadow: 8px 14px 26px rgba(0,0,0,0.28);
    overflow: hidden;
  }
  .card--front { background: var(--paper); }
  .card--back { background: var(--navy); }
  .pos-tl { left: 42px; top: 217px; }
  .pos-tr { left: 611px; top: 217px; }
  .pos-bl { left: 42px; top: 574px; }
  .pos-br { left: 611px; top: 574px; }

  .world-map {
    position: absolute;
    left: 28px; top: 45px;
    width: 480px; height: 240px;
    background: radial-gradient(ellipse at 55% 45%, var(--map) 0%, rgba(228,228,228,0.6) 55%, rgba(255,255,255,0) 75%);
  }

  .brand {
    position: absolute;
    display: flex;
    align-items: center;
    gap: 12px;
    font-weight: 500;
    white-space: nowrap;
  }
  .brand__dot { border-radius: 50%; background: var(--teal); flex: none; }
  .brand--front { left: 268px; top: 34px; font-size: 29px; color: var(--ink); letter-spacing: 0.5px; }
  .brand--front .brand__dot { width: 30px; height: 30px; }
  .license {
    position: absolute;
    left: 341px; top: 74px;
    font-size: 12px;
    letter-spacing: 2.4px;
    color: var(--teal);
  }

  .person { position: absolute; left: 42px; top: 130px; }
  .person__name { font-size: 21px; font-weight: 600; color: var(--ink); line-height: 1.1; }
  .person__name-zh { font-family: "Noto Sans TC", sans-serif; font-size: 18px; font-weight: 700; color: var(--ink); line-height: 1.2; }
  .person__title { font-size: 12.5px; color: var(--teal); margin-top: 6px; }

  .contacts { position: absolute; left: 300px; top: 198px; list-style: none; }
  .contacts li {
    display: flex; align-items: center; gap: 6px;
    height: 23.5px;
    font-size: 13px; color: var(--ink); letter-spacing: 0.8px;
  }
  .contacts svg { width: 11px; height: 11px; flex: none; }

  .branches { position: absolute; left: 51px; top: 38px; list-style: none; width: 434px; }
  .branches li {
    display: flex; align-items: center;
    height: 25.5px;
    color: #ffffff;
  }
  .branch__pin { width: 10px; height: 13px; margin-right: 6px; flex: none; }
  .branch__address { font-size: 10.5px; width: 230px; letter-spacing: -0.1px; }
  .branch__phone-icon { width: 9px; height: 13px; margin-left: 12px; margin-right: 8px; flex: none; }
  .branch__phone { font-size: 12.5px; letter-spacing: 1.6px; }
  .back-rule {
    position: absolute; left: 51px; top: 247px;
    width: 434px; height: 1px; background: var(--rule);
  }
  .brand--strip { left: 50%; transform: translateX(-50%); top: 260px; font-size: 21px; color: #ffffff; gap: 10px; }
  .brand--strip .brand__dot { width: 22px; height: 22px; }
  .brand--center { left: 50%; transform: translateX(-50%); top: 144px; font-size: 33px; color: #ffffff; gap: 14px; }
  .brand--center .brand__dot { width: 36px; height: 36px; }
</style>
</head>
<body>

<!-- Individual card, front with license -->
<section class="card card--front pos-tl">
  <div class="world-map" role="img" aria-label="Dotted world map in light grey"></div>
  <div class="brand brand--front"><span class="brand__dot"></span>MERIDAN</div>
  <div class="license">LICENSE NUMBER</div>
  <div class="person">
    <div class="person__name">Marcus Lee</div>
    <div class="person__name-zh">李明德</div>
    <div class="person__title">Director of Business Development</div>
  </div>
  <ul class="contacts">
    <li><svg viewBox="0 0 11 11"><rect x="2.5" y="0.5" width="6" height="10" rx="1" fill="none" stroke="#6cc5d6"/></svg>+852 5123 4870</li>
    <li><svg viewBox="0 0 11 11"><rect x="0.5" y="2" width="10" height="7" fill="#6cc5d6"/><path d="M0.5 2 L5.5 6 L10.5 2" fill="none" stroke="#fff"/></svg>marcus@meridan.com.hk</li>
    <li><svg viewBox="0 0 11 11"><circle cx="5.5" cy="5.5" r="4.5" fill="none" stroke="#6cc5d6"/><path d="M1 5.5 H10 M5.5 1 V10" stroke="#6cc5d6"/></svg>www.meridan.com.hk</li>
  </ul>
</section>

<!-- Individual card, front -->
<section class="card card--front pos-tr">
  <div class="world-map" role="img" aria-label="Dotted world map in light grey"></div>
  <div class="brand brand--front"><span class="brand__dot"></span>MERIDAN</div>
  <div class="person">
    <div class="person__name">Marcus Lee</div>
    <div class="person__name-zh">李明德</div>
    <div class="person__title">Director of Business Development</div>
  </div>
  <ul class="contacts">
    <li><svg viewBox="0 0 11 11"><rect x="2.5" y="0.5" width="6" height="10" rx="1" fill="none" stroke="#6cc5d6"/></svg>+852 5123 4870</li>
    <li><svg viewBox="0 0 11 11"><rect x="0.5" y="2" width="10" height="7" fill="#6cc5d6"/><path d="M0.5 2 L5.5 6 L10.5 2" fill="none" stroke="#fff"/></svg>marcus@meridan.com.hk</li>
    <li><svg viewBox="0 0 11 11"><circle cx="5.5" cy="5.5" r="4.5" fill="none" stroke="#6cc5d6"/><path d="M1 5.5 H10 M5.5 1 V10" stroke="#6cc5d6"/></svg>www.meridan.com.hk</li>
  </ul>
</section>

<!-- Individual card, back with branches -->
<section class="card card--back pos-bl">
  <ul class="branches">
    <li><svg class="branch__pin" viewBox="0 0 10 13"><path d="M5 0.5a4.5 4.5 0 0 1 4.5 4.5c0 3-4.5 7.5-4.5 7.5S0.5 8 0.5 5A4.5 4.5 0 0 1 5 0.5z" fill="#6cc5d6"/><circle cx="5" cy="5" r="1.7" fill="#263340"/></svg><span class="branch__address">12/F Harbour Point, 8-10 Canton Lane, Jordan</span><svg class="branch__phone-icon" viewBox="0 0 9 13"><rect x="0.5" y="0.5" width="8" height="12" rx="1.2" fill="none" stroke="#6cc5d6"/></svg><span class="branch__phone">+852 5123 4870</span></li>
    <li><svg class="branch__pin" viewBox="0 0 10 13"><path d="M5 0.5a4.5 4.5 0 0 1 4.5 4.5c0 3-4.5 7.5-4.5 7.5S0.5 8 0.5 5A4.5 4.5 0 0 1 5 0.5z" fill="#6cc5d6"/><circle cx="5" cy="5" r="1.7" fill="#263340"/></svg><span class="branch__address">12/F Harbour Point, 8-10 Canton Lane, Jordan</span><svg class="branch__phone-icon" viewBox="0 0 9 13"><rect x="0.5" y="0.5" width="8" height="12" rx="1.2" fill="none" stroke="#6cc5d6"/></svg><span class="branch__phone">+852 5123 4870</span></li>
    <li><svg class="branch__pin" viewBox="0 0 10 13"><path d="M5 0.5a4.5 4.5 0 0 1 4.5 4.5c0 3-4.5 7.5-4.5 7.5S0.5 8 0.5 5A4.5 4.5 0 0 1 5 0.5z" fill="#6cc5d6"/><circle cx="5" cy="5" r="1.7" fill="#263340"/></svg><span class="branch__address">12/F Harbour Point, 8-10 Canton Lane, Jordan</span><svg class="branch__phone-icon" viewBox="0 0 9 13"><rect x="0.5" y="0.5" width="8" height="12" rx="1.2" fill="none" stroke="#6cc5d6"/></svg><span class="branch__phone">+852 5123 4870</span></li>
    <li><svg class="branch__pin" viewBox="0 0 10 13"><path d="M5 0.5a4.5 4.5 0 0 1 4.5 4.5c0 3-4.5 7.5-4.5 7.5S0.5 8 0.5 5A4.5 4.5 0 0 1 5 0.5z" fill="#6cc5d6"/><circle cx="5" cy="5" r="1.7" fill="#263340"/></svg><span class="branch__address">12/F Harbour Point, 8-10 Canton Lane, Jordan</span><svg class="branch__phone-icon" viewBox="0 0 9 13"><rect x="0.5" y="0.5" width="8" height="12" rx="1.2" fill="none" stroke="#6cc5d6"/></svg><span class="branch__phone">+852 5123 4870</span></li>
    <li><svg class="branch__pin" viewBox="0 0 10 13"><path d="M5 0.5a4.5 4.5 0 0 1 4.5 4.5c0 3-4.5 7.5-4.5 7.5S0.5 8 0.5 5A4.5 4.5 0 0 1 5 0.5z" fill="#6cc5d6"/><circle cx="5" cy="5" r="1.7" fill="#263340"/></svg><span class="branch__address">12/F Harbour Point, 8-10 Canton Lane, Jordan</span><svg class="branch__phone-icon" viewBox="0 0 9 13"><rect x="0.5" y="0.5" width="8" height="12" rx="1.2" fill="none" stroke="#6cc5d6"/></svg><span class="branch__phone">+852 5123 4870</span></li>
    <li><svg class="branch__pin" viewBox="0 0 10 13"><path d="M5 0.5a4.5 4.5 0 0 1 4.5 4.5c0 3-4.5 7.5-4.5 7.5S0.5 8 0.5 5A4.5 4.5 0 0 1 5 0.5z" fill="#6cc5d6"/><circle cx="5" cy="5" r="1.7" fill="#263340"/></svg><span class="branch__address">12/F Harbour Point, 8-10 Canton Lane, Jordan</span><svg class="branch__phone-icon" viewBox="0 0 9 13"><rect x="0.5" y="0.5" width="8" height="12" rx="1.2" fill="none" stroke="#6cc5d6"/></svg><span class="branch__phone">+852 5123 4870</span></li>
    <li><svg class="branch__pin" viewBox="0 0 10 13"><path d="M5 0.5a4.5 4.5 0 0 1 4.5 4.5c0 3-4.5 7.5-4.5 7.5S0.5 8 0.5 5A4.5 4.5 0 0 1 5 0.5z" fill="#6cc5d6"/><circle cx="5" cy="5" r="1.7" fill="#263340"/></svg><span class="branch__address">12/F Harbour Point, 8-10 Canton Lane, Jordan</span><svg class="branch__phone-icon" viewBox="0 0 9 13"><rect x="0.5" y="0.5" width="8" height="12" rx="1.2" fill="none" stroke="#6cc5d6"/></svg><span class="branch__phone">+852 5123 4870</span></li>
    <li><svg class="branch__pin" viewBox="0 0 10 13"><path d="M5 0.5a4.5 4.5 0 0 1 4.5 4.5c0 3-4.5 7.5-4.5 7.5S0.5 8 0.5 5A4.5 4.5 0 0 1 5 0.5z" fill="#6cc5d6"/><circle cx="5" cy="5" r="1.7" fill="#263340"/></svg><span class="branch__address">12/F Harbour Point, 8-10 Canton Lane, Jordan</span><svg class="branch__phone-icon" viewBox="0 0 9 13"><rect x="0.5" y="0.5" width="8" height="12" rx="1.2" fill="none" stroke="#6cc5d6"/></svg><span class="branch__phone">+852 5123 4870</span></li>
  </ul>
  <div class="back-rule"></div>
  <div class="brand brand--strip"><span class="brand__dot"></span>MERIDAN</div>
</section>

<!-- Generic card, back -->
<section class="card card--back pos-br">
  <div class="brand brand--center"><span class="brand__dot"></span>MERIDAN</div>
</section>

</body>
</html>
```